We're Hiring Poster or Flyer design

We’re Hiring Details:

Positions include:
Office Manager
Office Assistant
Data Entry Techs
Outreach Manager
Asst. Outreach Manager
Events Coordinator
Drivers (must have personal car, insurance & Driver’s License)
Outreach Specialist—Walkers
Outreach Specialist—Phone/Telemarketing (evenings only)

Excellent Pay ! Fun Atmosphere ! Bonus Pay with Promotional & Career Advancement Opportunities

***************
need 3 formats of SAME flyer:
1) 8.5 x 11
2) 8.5 x 14
3) 11 x17

creative and eye catching a must; this flyer will be used on college bulletin boards and used to attract a younger demographic . . hip and chic look with "Americana style or political motif" preferred.

Target Market(s)

younger demographic . . flyer will be used during college recruiting fairs and in younger settings---age BRACKET is 21 - 35 Years old

Industry/Entity Type

Employment Agency

Font styles to use
Sans Serif

Colors

Designer to choose colors to be used in the design.

Requirements
Must have
• clean and attractive; hip; chic; simple and with good stock pics and layout
Nice to have
• american flag and patriotism
Should not have
• too much details on the job -- I only included the job announcement so you can get an idea of WHAT and WHO I am looking for . . don't list all the BORING details on the flyer/poster

```html
<!DOCTYPE html>
<html lang="en">
<head>
<meta charset="UTF-8">
<title>We Are Hiring — Marco Ellison for Mayor</title>
<link rel="stylesheet" href="https://fonts.googleapis.com/css2?family=Bebas+Neue&family=Arimo:wght@400;700&display=swap">
<style>
  :root {
    --sky-top: #a7c3d9;
    --sky-mid: #dfe8ef;
    --sky-haze: #eef2f5;
    --night: #000000;
    --headline-blue: #124a86;
    --ink: #111111;
    --accent-orange: #f07a2c;
    --paper-white: #ffffff;
  }
  * { margin: 0; padding: 0; box-sizing: border-box; }
  html, body { width: 849px; height: 1200px; overflow: hidden; background: var(--night); }
  .poster {
    position: relative;
    width: 849px;
    height: 1200px;
    overflow: hidden;
  }
  .backdrop {
    position: absolute;
    inset: 0;
    background: linear-gradient(180deg,
      var(--sky-top) 0%,
      var(--sky-mid) 28%,
      var(--sky-haze) 48%,
      #c9d3da 58%,
      #5d6770 64%,
      var(--night) 70%,
      var(--night) 100%);
  }
  .headline {
    position: absolute;
    left: 128px;
    top: 112px;
    font-family: "Bebas Neue", sans-serif;
    font-size: 188px;
    line-height: 152px;
    color: var(--headline-blue);
    letter-spacing: 2px;
  }
  .perks {
    position: absolute;
    left: 138px;
    top: 452px;
    font-family: "Bebas Neue", sans-serif;
    font-size: 37px;
    line-height: 39.5px;
    color: var(--ink);
    list-style: none;
  }
  .positions {
    position: absolute;
    left: 138px;
    top: 963px;
    font-family: "Arimo", sans-serif;
    color: var(--paper-white);
  }
  .positions-title {
    font-size: 10.5px;
    font-weight: 700;
    color: var(--accent-orange);
    margin-bottom: 2px;
  }
  .positions-list { list-style: none; }
  .positions-list li {
    position: relative;
    font-size: 11.5px;
    line-height: 14.4px;
    padding-left: 10px;
  }
  .positions-list li::before {
    content: "";
    position: absolute;
    left: 0;
    top: 5px;
    width: 4px;
    height: 4px;
    background: var(--accent-orange);
  }
  .positions-list .note {
    display: block;
    font-size: 7.5px;
    line-height: 9px;
  }
  .candidate-mark {
    position: absolute;
    left: 550px;
    top: 990px;
    width: 212px;
    font-family: "Arimo", sans-serif;
    font-weight: 700;
    color: var(--paper-white);
    text-align: center;
    font-size: 34px;
    line-height: 40px;
  }
</style>
</head>
<body>
  <main class="poster">
    <div class="backdrop" role="img" aria-label="Photograph of two hikers silhouetted on a mountain ridge, one helping the other up, above a sea of clouds under a pale blue sky"></div>

    <h1 class="headline">We Are<br>Hiring</h1>

    <ul class="perks">
      <li>Excellent Pay !</li>
      <li>Fun Atmosphere !</li>
      <li>Bonus Pay With</li>
      <li>Promotional &amp;</li>
      <li>Career Advancement</li>
      <li>Opportunities</li>
    </ul>

    <section class="positions">
      <h2 class="positions-title">POSITIONS INCLUDE:</h2>
      <ul class="positions-list">
        <li>Office Manager</li>
        <li>Office Assistant</li>
        <li>Data Entry Techs</li>
        <li>Outreach Manager</li>
        <li>Asst. Outreach Manager</li>
        <li>Events Coordinator</li>
        <li>Drivers<span class="note">(must have personal car, insurance &amp; Driver’s License)</span></li>
        <li>Outreach Specialist—Walkers</li>
        <li>Outreach Specialist—Phone/Telemarketing<span class="note">(evenings only)</span></li>
      </ul>
    </section>

    <div class="candidate-mark">Marco Ellison<br>MAYOR</div>
  </main>
</body>
</html>
```